Lark Stewardship Business Card design

We need a creative business card design for our hospitality management company
We need the following information:
Our business Logo: Lark Stewardship
Name: Mira Dalvorsen
Phone number: 0468 319 542
Email: mira@larkstewardship.com.au
Address: 214/53 Pemberly Street, South Melbourne 3206
Web: www.larkstewardship.com.au
I need the design to be a working file so that I can insert the names and numbers of the other staff members of our business.
The cards need to be 90 x 40mm
Thanks
Hospitality

```html
<!DOCTYPE html>
<html lang="en">
<head>
<meta charset="utf-8">
<title>Lark Stewardship Business Card</title>
<link rel="stylesheet" href="https://fonts.googleapis.com/css2?family=Oswald:wght@600&family=Source+Sans+3:wght@400&display=swap">
<style>
  :root {
    --board-dark: #b03a00;
    --board-mid: #cf6a00;
    --board-light: #d27a0a;
    --card-ink: #16161a;
    --card-paper: #ffffff;
    --gold: #e2a43a;
    --text-dark: #151515;
    --text-body: #222222;
    --text-light: #ffffff;
  }
  * { margin: 0; padding: 0; box-sizing: border-box; }
  html, body { width: 1200px; height: 907px; overflow: hidden; }
  body {
    position: relative;
    background: linear-gradient(135deg, var(--board-dark) 0%, var(--board-mid) 30%, var(--board-light) 60%, var(--board-mid) 85%, var(--board-dark) 100%);
    font-family: "Source Sans 3", "Myriad Pro", sans-serif;
  }
  .card {
    position: absolute;
    left: 234px;
    width: 730px;
    height: 324px;
    box-shadow: 2px 4px 8px rgba(0, 0, 0, 0.45);
    overflow: hidden;
  }
  .card--front { top: 105px; display: flex; }
  .card--back { top: 481px; background: var(--card-ink); }

  .brand-panel {
    position: relative;
    width: 317px;
    height: 100%;
    background: var(--card-ink);
  }
  .brand {
    position: absolute;
    left: 0; right: 0; top: 124px;
    display: flex;
    align-items: center;
    justify-content: center;
    gap: 12px;
  }
  .brand__mark {
    width: 20px; height: 20px;
    background: var(--gold);
  }
  .brand__name {
    font-family: "Oswald", "Arial Narrow", sans-serif;
    font-weight: 600;
    font-size: 28px;
    line-height: 1;
    text-transform: uppercase;
    color: var(--gold);
    letter-spacing: 0.2px;
  }
  .website {
    position: absolute;
    left: 0; right: 0; top: 262px;
    text-align: center;
    font-size: 17px;
    color: var(--text-light);
  }

  .contact-panel {
    flex: 1;
    background: var(--card-paper);
    padding: 128px 0 0 35px;
  }
  .person-name {
    font-family: "Oswald", "Arial Narrow", sans-serif;
    font-weight: 600;
    font-size: 31px;
    line-height: 1;
    text-transform: uppercase;
    color: var(--text-dark);
    margin-bottom: 22px;
    margin-top: -2px;
  }
  .contact-list { list-style: none; }
  .contact-list li {
    font-size: 17.5px;
    line-height: 26px;
    color: var(--text-body);
  }

  .back-brand {
    position: absolute;
    right: 48px;
    bottom: 56px;
    display: flex;
    align-items: center;
    gap: 18px;
  }
  .back-brand__mark {
    width: 38px; height: 38px;
    background: var(--gold);
  }
  .back-brand__name {
    font-family: "Oswald", "Arial Narrow", sans-serif;
    font-weight: 600;
    font-size: 52px;
    line-height: 1;
    text-transform: uppercase;
    color: var(--gold);
  }
</style>
</head>
<body>
  <section class="card card--front">
    <div class="brand-panel">
      <div class="brand">
        <span class="brand__mark"></span>
        <span class="brand__name">Lark Stewardship</span>
      </div>
      <p class="website">www.larkstewardship.com.au</p>
    </div>
    <div class="contact-panel">
      <h1 class="person-name">Mira Dalvorsen</h1>
      <ul class="contact-list">
        <li>Phone number: 0468 319 542</li>
        <li>Email: mira@larkstewardship.com.au</li>
        <li>Address: 214/53 Pemberly Street,</li>
        <li>South Melbourne 3206</li>
      </ul>
    </div>
  </section>

  <section class="card card--back">
    <div class="back-brand">
      <span class="back-brand__mark"></span>
      <span class="back-brand__name">Lark Stewardship</span>
    </div>
  </section>
</body>
</html>
```